Nur Briefpapier und VK für Pflegedienst, Logo vorhanden!!!!
Zielgruppe
Wir sind ein Pflegedienst, unsere Zielgruppe sind Krankenkassen und Patienten und andere Krankenhäuser mit denen wir zusammen arbeiten.
Aufgabenstellung
modern, seriös, elitär

```html
<!DOCTYPE html>
<html lang="de">
<head>
<meta charset="utf-8">
<title>Renofleet Pflegedienst – Briefpapier</title>
<link rel="stylesheet" href="https://fonts.googleapis.com/css2?family=Arimo:wght@400;700&display=swap">
<style>
  :root {
    --brand-red: #f2333f;
    --brand-red-faint: #fbd3d6;
    --paper: #ffffff;
    --footer-text: #ffffff;
    --fold-mark: #f2333f;
  }
  * { margin: 0; padding: 0; box-sizing: border-box; }
  html, body { width: 850px; height: 1200px; overflow: hidden; background: var(--paper); }
  body { font-family: "Arimo", Arial, sans-serif; }

  .letterhead {
    position: relative;
    width: 850px;
    height: 1200px;
    background: var(--paper);
    overflow: hidden;
  }

  .header-band {
    position: absolute;
    top: 0; left: 0;
    width: 100%;
    height: 133px;
    background: var(--brand-red);
  }

  .brand {
    position: absolute;
    top: 170px;
    right: 78px;
    text-align: right;
    color: var(--brand-red);
    font-weight: 700;
    line-height: 1;
  }
  .brand-name { font-size: 48px; letter-spacing: 1px; }
  .brand-tagline { font-size: 24px; margin-top: 10px; }

  .brand-watermark {
    position: absolute;
    top: 560px;
    left: 0;
    width: 100%;
    text-align: center;
    color: var(--brand-red-faint);
    font-weight: 700;
    font-size: 96px;
    letter-spacing: 2px;
  }

  .fold-mark {
    position: absolute;
    left: 0;
    width: 15px;
    height: 1px;
    background: var(--fold-mark);
  }
  .fold-mark--upper { top: 429px; }
  .fold-mark--lower { top: 596px; }

  .footer-band {
    position: absolute;
    left: 0; bottom: 0;
    width: 100%;
    height: 152px;
    background: var(--brand-red);
    color: var(--footer-text);
  }
  .footer-column {
    position: absolute;
    top: 20px;
    font-size: 14.5px;
    line-height: 19.5px;
    font-style: normal;
  }
  .footer-column--address { left: 101px; }
  .footer-column--management { left: 318px; }
  .footer-column--bank { left: 551px; }
</style>
</head>
<body>
  <main class="letterhead">
    <div class="header-band"></div>

    <div class="brand">
      <div class="brand-name">Renofleet</div>
      <div class="brand-tagline">Pflegedienste</div>
    </div>

    <div class="brand-watermark" aria-hidden="true">Renofleet</div>

    <span class="fold-mark fold-mark--upper"></span>
    <span class="fold-mark fold-mark--lower"></span>

    <footer class="footer-band">
      <address class="footer-column footer-column--address">
        Renofleet Pflegedienst<br>
        Musterstraße 123<br>
        12345 Musterstadt<br>
        www.muster.de
      </address>
      <div class="footer-column footer-column--management">
        Geschäftsführung<br>
        Max Mustermann<br>
        0123456789<br>
        info@muster.de
      </div>
      <div class="footer-column footer-column--bank">
        Musterbank<br>
        BIC: MusterBIC<br>
        IBAN: MusterIBAN<br>
        Steuer-Nr. 1234567890
      </div>
    </footer>
  </main>
</body>
</html>
```